Sports and football Live scores website

Hey designers, I want a website which will feature live football and other sports events on demand and on the go. This website should be similar to http://pitchtally.example
As the football events are been played, my website will be giving live updates of the events. There will be different categories such as football, basket, tennis and others as the website above. Also, there will be menu for top footballing nations as also show in the website above. My website should refresh it's self every one minutes. The proposed live score website should be youthful and attractive. Bright colors such me used as my target audience are sports lovers.

```html
<!DOCTYPE html>
<html lang="en">
<head>
<meta charset="utf-8">
<title>KICKRALLY – Live Scores</title>
<link href="https://fonts.googleapis.com/css2?family=Oswald:wght@500;700&family=Roboto:wght@400;500;700&display=swap" rel="stylesheet">
<style>
:root{
  --page:#1c262e;
  --stadium-top:#3a4a57;
  --stadium-mid:#22303a;
  --panel:#28333c;
  --row-a:#2b3640;
  --row-b:#25303a;
  --line:#34414c;
  --text:#cfd6dc;
  --muted:#8e9aa4;
  --white:#ffffff;
  --accent:#f08a1c;
  --accent-dark:#c9690c;
  --hero-sky:#6f8fab;
  --hero-grass:#3f6b2e;
}
*{margin:0;padding:0;box-sizing:border-box}
html,body{width:720px;height:1200px;overflow:hidden}
body{
  background:linear-gradient(180deg,var(--stadium-top) 0,var(--stadium-mid) 260px,var(--page) 340px,var(--page) 100%);
  font-family:"Roboto",Arial,sans-serif;color:var(--text);position:relative;
}
.site-header{position:absolute;top:0;left:0;width:720px;height:62px}
.brand{position:absolute;left:80px;top:28px;display:flex;align-items:center;gap:6px;
  font-family:"Oswald",sans-serif;font-weight:700;font-size:15px;color:var(--white);letter-spacing:1px}
.brand-dot{width:12px;height:12px;border-radius:50%;background:var(--accent)}
.tagline{position:absolute;right:78px;top:12px;font-size:6px;color:var(--accent);letter-spacing:.5px;font-weight:500}
.main-nav{position:absolute;left:210px;top:38px;display:flex;gap:13px}
.main-nav a{font-size:6.5px;color:var(--text);text-decoration:none;font-weight:500;letter-spacing:.4px}
.main-nav a.active{color:var(--accent)}
.hero{position:absolute;left:78px;top:72px;width:560px;height:228px;overflow:hidden;
  border:2px solid #51616d}
.hero-photo{position:absolute;inset:0;
  background:radial-gradient(ellipse at 70% 35%,#c9d6e0 0,var(--hero-sky) 35%,#3c5368 70%),var(--hero-sky)}
.hero-photo::after{content:"";position:absolute;left:0;right:0;bottom:0;height:70px;
  background:linear-gradient(180deg,rgba(63,107,46,0),var(--hero-grass))}
.hero-copy{position:absolute;left:52px;top:42px;width:210px}
.hero-title{font-family:"Oswald",sans-serif;font-weight:700;font-size:29px;line-height:30px;color:var(--white);text-transform:uppercase}
.hero-text{margin-top:8px;font-size:7px;line-height:10px;color:#e6ecf1}
.hero-btn{display:inline-block;margin-top:12px;background:var(--accent);color:var(--white);
  font-size:6.5px;font-weight:700;padding:6px 11px;text-transform:uppercase}
.side-nav{position:absolute;left:86px;top:322px;width:70px}
.side-nav ul{list-style:none;margin-bottom:11px}
.side-nav li{font-size:6.5px;line-height:11.3px;color:var(--text)}
.fixtures{position:absolute;left:174px;top:320px;width:338px;display:flex;flex-direction:column;gap:10px}
.league-head{height:18px;background:var(--accent);display:flex;justify-content:space-between;align-items:center;
  padding:0 8px;font-size:7px;font-weight:700;color:var(--white)}
.league-head .date{font-weight:400;font-size:6px}
.match{height:20px;display:grid;grid-template-columns:34px 1fr 34px 1fr 14px;align-items:center;
  padding:0 8px;font-size:6.5px;background:var(--row-a);border-bottom:1px solid var(--line)}
.match:nth-child(odd){background:var(--row-b)}
.match .time{color:var(--muted)}
.match .home{text-align:right}
.match .score{text-align:center;color:var(--accent);font-weight:700}
.match .mark{width:5px;height:5px;border-radius:50%;background:var(--muted);justify-self:end}
.aside{position:absolute;left:518px;top:320px;width:122px}
.ad{height:160px;position:relative;overflow:hidden}
.ad-ball{background:radial-gradient(circle at 35% 50%,#e9eef2 0,#9aa6ae 30%,#2f4a2a 60%,#1d2f1a 100%)}
.ad-fire{height:156px;background:radial-gradient(circle at 60% 40%,#ffcf5a 0,#f0781a 35%,#8a2a0c 70%,#3a1408 100%)}
.ad-label{position:absolute;right:8px;top:52px;font-family:"Oswald",sans-serif;font-weight:700;
  font-size:16px;line-height:17px;color:var(--white);text-align:right}
.ad-fire .ad-label{left:10px;right:auto;top:98px;text-align:left;font-size:14px}
.standings{margin:18px 0 52px;width:122px;border-collapse:collapse;font-size:6px}
.standings th{background:var(--accent);color:var(--white);text-align:left;padding:4px 4px;font-weight:700}
.standings th.num,.standings td.num{text-align:center;width:16px}
.standings td{padding:0 4px;height:15px;border-bottom:1px solid var(--line);background:var(--row-a)}
.standings tr:nth-child(even) td{background:var(--row-b)}
.site-footer{position:absolute;left:0;top:1168px;width:720px;text-align:center;font-size:6px;color:var(--muted)}
</style>
</head>
<body>
<header class="site-header">
  <div class="brand"><span class="brand-dot"></span>KICKRALLY</div>
  <div class="tagline">FOOTBALL LIVE RESULTS</div>
  <nav class="main-nav">
    <a class="active">HOME</a><a>LIVE SCORE</a><a>SOCCER</a><a>BASKETBALL</a><a>TENNIS</a><a>CRICKET</a><a>HOCKEY</a><a>HANDBALL</a><a>MOBILE</a><a>CONTACT</a>
  </nav>
</header>

<section class="hero">
  <div class="hero-photo" role="img" aria-label="Photo of two footballers challenging for a ball in a stadium"></div>
  <div class="hero-copy">
    <h1 class="hero-title">Find the best<br>odds</h1>
    <p class="hero-text">Live scores, fixtures and odds from every league, updated each minute wherever you are.</p>
    <span class="hero-btn">Read more</span>
  </div>
</section>

<nav class="side-nav">
  <ul><li>Home</li><li>Live</li><li>Live Tables</li><li>My Matches</li><li>Top Leagues</li><li>Champions Cup</li><li>Europe Cup</li><li>World Cup</li><li>Copa Cup</li><li>Friendlies</li><li>Internationals</li></ul>
  <ul><li>England</li><li>Italy</li><li>Spain</li><li>Germany</li><li>France</li><li>Netherlands</li><li>Belgium</li><li>Portugal</li><li>Scotland</li></ul>
  <ul><li>Olympics Men</li><li>Olympics Women</li><li>Euro U21</li><li>World Cup U20</li><li>World Cup U17</li><li>Euro U19</li><li>Euro U17</li><li>World Cup Women</li><li>Euro Women</li></ul>
  <ul><li>Belarus</li><li>Bosnia</li><li>Bulgaria</li><li>Croatia</li><li>Czech Republic</li><li>Greece</li><li>Hungary</li><li>Israel</li><li>Latvia</li><li>Lithuania</li><li>Montenegro</li><li>Poland</li><li>Romania</li><li>Russia</li><li>Serbia</li><li>Slovakia</li><li>Sweden</li><li>Ukraine</li></ul>
</nav>

<main class="fixtures">
  <section class="league">
    <div class="league-head"><span>Olympics Men - Final</span><span class="date">August 17</span></div>
    <div class="match"><span class="time">20:30</span><span class="home">Brasil U21</span><span class="score">-</span><span>Germany U21</span><span class="mark"></span></div>
  </section>
  <section class="league">
    <div class="league-head"><span>Olympics Men - 3rd place</span><span class="date">August 17</span></div>
    <div class="match"><span class="time">17:00</span><span class="home">Brasil U21</span><span class="score">-</span><span>Germany U21</span><span class="mark"></span></div>
  </section>
  <section class="league">
    <div class="league-head"><span>England - Top League</span><span class="date">August 19</span></div>
    <div class="match"><span class="time">13:30</span><span class="home">Stonebridge City</span><span class="score">-</span><span>Marlow City</span><span class="mark"></span></div>
    <div class="match"><span class="time">16:00</span><span class="home">Burnholt</span><span class="score">-</span><span>Lakepool</span><span class="mark"></span></div>
    <div class="match"><span class="time">16:00</span><span class="home">Seaford City</span><span class="score">-</span><span>Holt City</span><span class="mark"></span></div>
    <div class="match"><span class="time">16:00</span><span class="home">Thornbury Rovers</span><span class="score">-</span><span>Crown Palace</span><span class="mark"></span></div>
    <div class="match"><span class="time">16:00</span><span class="home">Wetford</span><span class="score">-</span><span>Chesley</span><span class="mark"></span></div>
    <div class="match"><span class="time">18:30</span><span class="home">Hadderton Town</span><span class="score">-</span><span>Brightmoor Albion</span><span class="mark"></span></div>
    <div class="match"><span class="time">18:30</span><span class="home">Lakepool</span><span class="score">-</span><span>Wolvercote Wanderers</span><span class="mark"></span></div>
  </section>
  <section class="league">
    <div class="league-head"><span>England - Championship</span><span class="date">August 19</span></div>
    <div class="match"><span class="time">13:30</span><span class="home">Stonebridge City</span><span class="score">-</span><span>Marlow City</span><span class="mark"></span></div>
    <div class="match"><span class="time">16:00</span><span class="home">Burnholt</span><span class="score">-</span><span>Lakepool</span><span class="mark"></span></div>
    <div class="match"><span class="time">16:00</span><span class="home">Seaford City</span><span class="score">-</span><span>Holt City</span><span class="mark"></span></div>
    <div class="match"><span class="time">16:00</span><span class="home">Thornbury Rovers</span><span class="score">-</span><span>Crown Palace</span><span class="mark"></span></div>
    <div class="match"><span class="time">16:00</span><span class="home">Wetford</span><span class="score">-</span><span>Chesley</span><span class="mark"></span></div>
    <div class="match"><span class="time">18:30</span><span class="home">Hadderton Town</span><span class="score">-</span><span>Brightmoor Albion</span><span class="mark"></span></div>
    <div class="match"><span class="time">18:30</span><span class="home">Lakepool</span><span class="score">-</span><span>Wolvercote Wanderers</span><span class="mark"></span></div>
  </section>
  <section class="league">
    <div class="league-head"><span>England - Top League</span><span class="date">August 20</span></div>
    <div class="match"><span class="time">13:30</span><span class="home">Stonebridge City</span><span class="score">-</span><span>Marlow City</span><span class="mark"></span></div>
    <div class="match"><span class="time">16:00</span><span class="home">Burnholt</span><span class="score">-</span><span>Lakepool</span><span class="mark"></span></div>
    <div class="match"><span class="time">16:00</span><span class="home">Seaford City</span><span class="score">-</span><span>Holt City</span><span class="mark"></span></div>
    <div class="match"><span class="time">16:00</span><span class="home">Thornbury Rovers</span><span class="score">-</span><span>Crown Palace</span><span class="mark"></span></div>
    <div class="match"><span class="time">16:00</span><span class="home">Wetford</span><span class="score">-</span><span>Chesley</span><span class="mark"></span></div>
    <div class="match"><span class="time">18:30</span><span class="home">Hadderton Town</span><span class="score">-</span><span>Brightmoor Albion</span><span class="mark"></span></div>
    <div class="match"><span class="time">18:30</span><span class="home">Lakepool</span><span class="score">-</span><span>Wolvercote Wanderers</span><span class="mark"></span></div>
  </section>
  <section class="league">
    <div class="league-head"><span>England - Championship</span><span class="date">August 20</span></div>
    <div class="match"><span class="time">13:30</span><span class="home">Stonebridge City</span><span class="score">-</span><span>Marlow City</span><span class="mark"></span></div>
    <div class="match"><span class="time">16:00</span><span class="home">Burnholt</span><span class="score">-</span><span>Lakepool</span><span class="mark"></span></div>
    <div class="match"><span class="time">16:00</span><span class="home">Seaford City</span><span class="score">-</span><span>Holt City</span><span class="mark"></span></div>
    <div class="match"><span class="time">16:00</span><span class="home">Thornbury Rovers</span><span class="score">-</span><span>Crown Palace</span><span class="mark"></span></div>
    <div class="match"><span class="time">18:30</span><span class="home">Wetford</span><span class="score">-</span><span>Chesley</span><span class="mark"></span></div>
  </section>
  <section class="league">
    <div class="league-head"><span>Olympics Men - Final</span><span class="date">August 21</span></div>
    <div class="match"><span class="time">20:30</span><span class="home">Brasil U21</span><span class="score">-</span><span>Germany U21</span><span class="mark"></span></div>
    <div class="match"><span class="time">20:30</span><span class="home">Brasil U21</span><span class="score">-</span><span>Germany U21</span><span class="mark"></span></div>
  </section>
</main>

<aside class="aside">
  <div class="ad ad-ball" role="img" aria-label="Promotional photo of a football on a pitch">
    <span class="ad-label">100%<br>Bonus</span>
  </div>
  <table class="standings">
    <thead><tr><th>Standings</th><th class="num">P</th><th class="num">Pts</th></tr></thead>
    <tbody>
      <tr><td>1. Marlow City</td><td class="num">3</td><td class="num">9</td></tr>
      <tr><td>2. Lakepool</td><td class="num">3</td><td class="num">7</td></tr>
      <tr><td>3. Chesley</td><td class="num">3</td><td class="num">7</td></tr>
      <tr><td>4. Crown Palace</td><td class="num">3</td><td class="num">6</td></tr>
      <tr><td>5. Holt City</td><td class="num">3</td><td class="num">5</td></tr>
      <tr><td>6. Wetford</td><td class="num">3</td><td class="num">4</td></tr>
      <tr><td>7. Burnholt</td><td class="num">3</td><td class="num">3</td></tr>
      <tr><td>8. Seaford City</td><td class="num">3</td><td class="num">1</td></tr>
    </tbody>
  </table>
  <div class="ad ad-fire" role="img" aria-label="Promotional illustration of a footballer kicking a flaming ball">
    <span class="ad-label">Turn the<br>Betting</span>
  </div>
</aside>

<footer class="site-footer">© 2018 KICKRALLY ALL RIGHTS RESERVED</footer>
</body>
</html>
```